Kem7Dex Letterhead

Need a new letterhead for my law firm.
IDENTIFYING INFORMATION BELOW:
Ansel T Brightwater III
Attorney at Law
Address: 4832 Tillbury Rd, Ste 250, Dallas, TX 75204
Phone: 866-402-7183
Fax: 469-583-0271
Email: kem@kem7dex.example
Website: www.kem7dex.example

Colors
0054AA
0677BA
7BADD7
CADEEF
E8F1F8

Requirements
Must have
• Logo needs to be on the letterhead, along with identifying information which is included in the project description.

```html
<!DOCTYPE html>
<html lang="en">
<head>
<meta charset="utf-8">
<title>Kem7Dex Letterhead</title>
<link href="https://fonts.googleapis.com/css2?family=Arimo:wght@400;700&display=swap" rel="stylesheet">
<style>
  :root {
    --backdrop: #ececec;
    --paper: #ffffff;
    --ink: #1a1a1a;
    --body-ink: #3c3c3c;
    --rule: #111111;
    --blue-deep: #0054AA;
    --blue: #0677BA;
    --blue-light: #7BADD7;
    --blue-pale: #CADEEF;
    --blue-mist: #E8F1F8;
  }
  * { box-sizing: border-box; margin: 0; padding: 0; }
  html, body {
    width: 1200px; height: 795px; overflow: hidden;
    background: var(--backdrop);
    font-family: "Arimo", Arial, sans-serif;
  }
  .letterhead {
    position: absolute; left: 333px; top: 20px;
    width: 534px; height: 755px;
    background: var(--paper);
    box-shadow: 0 2px 10px rgba(0,0,0,.12);
  }
  .edge-band {
    position: absolute; left: 0; top: 0; width: 7px; height: 100%;
    background: var(--rule);
  }
  .edge-band__accent {
    position: absolute; left: 0; top: 80%; width: 100%; height: 12%;
    background: linear-gradient(180deg, var(--blue-deep), var(--blue));
  }
  .brand { position: absolute; left: 52px; top: 48px; }
  .brand__name {
    font-weight: 700; font-size: 20px; letter-spacing: .3px;
    color: var(--ink); line-height: 1;
  }
  .brand__tagline {
    margin-top: 4px; font-size: 7px; letter-spacing: 1px;
    color: var(--body-ink);
  }
  .letter-body {
    position: absolute; left: 52px; top: 150px; width: 400px;
    color: var(--body-ink); font-size: 7.6px; line-height: 11px;
  }
  .letter-body__salutation { font-size: 10px; margin-bottom: 14px; color: var(--ink); }
  .letter-body p { margin-bottom: 11px; }
  .letter-body__closing { margin-top: 14px; }
  .signature {
    display: block; width: 90px; height: 34px; margin-top: 6px;
    background: linear-gradient(90deg, var(--paper), #e4e4e4 50%, var(--paper));
  }
  .sender { position: absolute; left: 52px; top: 548px; }
  .sender__name {
    font-weight: 700; font-size: 11px; letter-spacing: .4px;
    color: var(--ink); text-transform: uppercase;
  }
  .sender__title { font-size: 8px; color: var(--blue); margin-top: 2px; }
  .sender__divider { width: 26px; height: 1px; background: var(--ink); margin: 12px 0 10px; }
  .contact-list { list-style: none; font-size: 8px; color: var(--ink); line-height: 11px; }
  .contact-list li { display: flex; align-items: flex-start; gap: 6px; }
  .contact-list svg { width: 8px; height: 8px; margin-top: 1.5px; flex: none; fill: var(--blue); }
</style>
</head>
<body>
<main class="letterhead">
  <div class="edge-band"><div class="edge-band__accent"></div></div>

  <header class="brand">
    <div class="brand__name">Kem7Dex</div>
    <div class="brand__tagline">Counsel you can trust</div>
  </header>

  <section class="letter-body">
    <div class="letter-body__salutation">Dear Mr. Hartwell,</div>
    <p>Lorem ipsum dolor sit amet, consectetur adipiscing elit. Donec orci purus, luctus vitae dignissim eu, iaculis sed purus. Vivamus faucibus, ipsum nec aliquet viverra, leo mauris condimentum ligula, sit amet sagittis enim ligula quis arcu. Nam egestas tortor id nisi porttitor mattis. In tortor ante, ultricies in suscipit a, tempus non massa. Vivamus et auctor mi. Fusce vel massa nulla. Phasellus nec eros mauris, et scelerisque orci.</p>
    <p>Donec malesuada orci vitae nulla accumsan porta a id massa. Quisque accumsan iaculis magna sit amet fringilla. Maecenas consequat, magna eget tincidunt semper, odio nibh rutrum mi, id feugiat ante nisl eu risus. Vestibulum nunc orci, rhoncus a placerat in, ultricies in mi. Cras mattis varius eros, vel fringilla nisi suscipit eget. Quisque scelerisque sagittis nulla at porttitor.</p>
    <p>Sed id augue vitae urna euismod commodo aliquet a quam. Pellentesque arcu velit, cursus et malesuada ut, consequat et diam. Nullam erat sem, rhoncus id ullamcorper vitae, rhoncus et arcu. In ultricies ultricies nulla, ut rutrum nisl iaculis at. Donec eu magna a metus ornare faucibus. Fusce aliquet faucibus ultricies. Morbi semper, est id tincidunt gravida, sem arcu adipiscing lacus, ac bibendum nulla leo eu purus. Quisque nec diam sed risus consectetur accumsan quis quis nibh. Vestibulum id purus lorem.</p>
    <div class="letter-body__closing">Sincerely,</div>
    <span class="signature" role="img" aria-label="Handwritten signature of the attorney"></span>
  </section>

  <footer class="sender">
    <div class="sender__name">Ansel T Brightwater III</div>
    <div class="sender__title">Attorney at Law</div>
    <div class="sender__divider"></div>
    <ul class="contact-list">
      <li><svg viewBox="0 0 10 10"><path d="M2 0.5h2l1 2.5-1.3 1a5 5 0 0 0 2.3 2.3l1-1.3 2.5 1v2a1 1 0 0 1-1 1A8.5 8.5 0 0 1 1 1.5a1 1 0 0 1 1-1z"/></svg>866-402-7183</li>
      <li><svg viewBox="0 0 10 10"><rect x="2.5" y="0.5" width="5" height="3"/><rect x="0.5" y="4" width="9" height="4" rx="1"/><rect x="2.5" y="7" width="5" height="2.5"/></svg>469-583-0271</li>
      <li><svg viewBox="0 0 10 10"><path d="M0.5 2h9v6h-9z M0.5 2l4.5 3.5 4.5-3.5" fill="none" stroke="var(--blue)" stroke-width="1.2"/></svg>kem@kem7dex.example</li>
      <li><svg viewBox="0 0 10 10"><g fill="none" stroke="var(--blue)" stroke-width="1"><circle cx="5" cy="5" r="4.2"/><ellipse cx="5" cy="5" rx="1.8" ry="4.2"/><path d="M0.8 5h8.4"/></g></svg>www.kem7dex.example</li>
      <li><svg viewBox="0 0 10 10"><path d="M5 0.5a3.5 3.5 0 0 1 3.5 3.5c0 2.5-3.5 5.5-3.5 5.5S1.5 6.5 1.5 4A3.5 3.5 0 0 1 5 0.5zm0 2a1.4 1.4 0 1 0 0 2.8 1.4 1.4 0 0 0 0-2.8z"/></svg><span>4832 Tillbury Rd, Ste 250<br>Dallas, TX 75204</span></li>
    </ul>
  </footer>
</main>
</body>
</html>
```